Business Card Design Project

Keep it simple , using logo and colors that compliment. Logo on one side with complimentary back ground color. Other side, personal info with possible complimentary design/colors

Target Market(s)

we are a non for profit that will be seeking donations . Both monetary and in kind

Industry/Entity Type

Business

Font styles to use
Sans Serif

Colors

Designer to choose colors to be used in the design.

```html
<!DOCTYPE html>
<html lang="en">
<head>
<meta charset="utf-8">
<title>Bright Path Fund – Business Card</title>
<link rel="stylesheet" href="https://fonts.googleapis.com/css2?family=Source+Sans+3:wght@300;400&display=swap">
<style>
  :root {
    --backdrop: #e8e3dc;
    --card-navy: #212a45;
    --accent-yellow: #f5e10a;
    --card-shadow: rgba(0, 0, 0, 0.35);
  }
  * { box-sizing: border-box; margin: 0; padding: 0; }
  html, body {
    width: 1200px;
    height: 800px;
    overflow: hidden;
    background: var(--backdrop);
    font-family: "Source Sans 3", "Helvetica Neue", Arial, sans-serif;
  }
  .canvas {
    position: relative;
    width: 1200px;
    height: 800px;
  }
  .card {
    position: absolute;
    left: 282px;
    width: 498px;
    height: 290px;
    background: var(--card-navy);
    border-radius: 12px;
    box-shadow: 0 6px 14px var(--card-shadow);
  }
  .card--front { top: 122px; }
  .card--back  { top: 428px; }
  .card__frame {
    position: absolute;
    inset: 16px;
    border: 3px solid var(--accent-yellow);
    border-radius: 12px;
  }
  .brand {
    position: absolute;
    left: 0;
    right: 0;
    top: 127px;
    display: flex;
    align-items: center;
    justify-content: center;
    gap: 12px;
  }
  .brand__dot {
    width: 14px;
    height: 14px;
    border-radius: 50%;
    background: var(--accent-yellow);
    flex: none;
  }
  .brand__name {
    color: var(--accent-yellow);
    font-weight: 300;
    font-size: 28px;
    line-height: 34px;
    letter-spacing: 0.01em;
    white-space: nowrap;
  }
  .contact {
    position: absolute;
    right: 51px;
    top: 124px;
    color: var(--accent-yellow);
    text-align: right;
    font-weight: 400;
  }
  .contact__name {
    font-size: 15.5px;
    letter-spacing: 0.02em;
    text-transform: uppercase;
    line-height: 20px;
  }
  .contact__title {
    font-size: 12.5px;
    line-height: 18px;
  }
  .contact__list {
    list-style: none;
    margin-top: 15px;
  }
  .contact__item {
    display: flex;
    justify-content: flex-end;
    align-items: center;
    gap: 8px;
    font-size: 12.5px;
    line-height: 17.5px;
    white-space: nowrap;
  }
  .contact__icon {
    width: 14px;
    height: 14px;
    flex: none;
    fill: var(--accent-yellow);
  }
</style>
</head>
<body>
<main class="canvas">
  <section class="card card--front" aria-label="Card front">
    <div class="card__frame"></div>
    <div class="brand">
      <span class="brand__dot" aria-hidden="true"></span>
      <span class="brand__name">Bright Path Fund</span>
    </div>
  </section>

  <section class="card card--back" aria-label="Card back">
    <div class="card__frame"></div>
    <div class="contact">
      <p class="contact__name">Nora Whitfield</p>
      <p class="contact__title">General Manager</p>
      <ul class="contact__list">
        <li class="contact__item">555 014 2290
          <svg class="contact__icon" viewBox="0 0 16 16" aria-hidden="true"><path d="M3.5 1.5l2.3 2.6-1.2 1.8c.9 2 2.5 3.6 4.5 4.5l1.8-1.2 2.6 2.3-1.4 2C7.6 13.2 2.8 8.4 1.5 2.9z"/></svg>
        </li>
        <li class="contact__item">555 014 2291
          <svg class="contact__icon" viewBox="0 0 16 16" aria-hidden="true"><path d="M4.5 1h7a1 1 0 0 1 1 1v12a1 1 0 0 1-1 1h-7a1 1 0 0 1-1-1V2a1 1 0 0 1 1-1zm.8 2v8.5h5.4V3zM8 12.3a.9.9 0 1 0 0 1.8.9.9 0 0 0 0-1.8z"/></svg>
        </li>
        <li class="contact__item">nora@brightpathfund.com
          <svg class="contact__icon" viewBox="0 0 16 16" aria-hidden="true"><path d="M1 3.5h14v1L8 9 1 4.5zM1 6l7 4.5L15 6v6.5H1z"/></svg>
        </li>
        <li class="contact__item">www.brightpathfund.com
          <svg class="contact__icon" viewBox="0 0 16 16" aria-hidden="true"><path d="M8 1a7 7 0 1 0 0 14A7 7 0 0 0 8 1zm-1 2.2c.3.9-.4 1.6-1.2 2-.9.4-.6 1.5.3 1.7.9.2 1.2 1 .8 1.8-.4.9-.2 2 .5 2.6.5.4.3 1.3-.3 1.5A5.6 5.6 0 0 1 7 3.2zm2.5 1c1 .2 2.3 1 2.9 2.1-.6.3-1.4.1-1.8-.5-.4-.5-1-.7-1.1-1.6z"/></svg>
        </li>
      </ul>
    </div>
  </section>
</main>
</body>
</html>
```